TBrandow executive consulting

We need a basic clean website for executive consulting. Rosalind is the previos CIO for bluecrest skyways and currently supports several technology companies with innovation and transformation.

Target Market(s)

C level technology and CIO training

Industry/Entity Type

Technology and travel industry

Coding

Coded - Design and coding required

Number of Pages Required

3 page

Font styles to use
Sans Serif

Colors
0054AA
0677BA
7BADD7
CADEEF
E8F1F8
0094D4
00A9DD
6FCCEA
C7EBF8
E9F6FB

Requirements
Must have
• Home page, about us, services social media links

```html
<!DOCTYPE html>
<html lang="en">
<head>
<meta charset="utf-8">
<title>TBrandow Executive Consulting</title>
<link rel="stylesheet" href="https://fonts.googleapis.com/css2?family=Poppins:wght@300;400;500;600&family=PT+Serif:wght@400;700&display=swap">
<style>
:root{
  --accent:#00A9DD;
  --accent-deep:#0094D4;
  --ink:#222;
  --text:#444;
  --muted:#555;
  --dark:#333538;
  --soft:#f4f4f4;
  --pale:#E8F1F8;
  --white:#fff;
}
*{box-sizing:border-box;margin:0;padding:0}
html,body{width:1200px;height:3783px;overflow:hidden}
body{font-family:'Poppins',sans-serif;color:var(--text);background:var(--white);position:relative}
.abs{position:absolute}

/* top bar + header */
.topbar{left:0;top:0;width:1200px;height:53px;background:var(--dark)}
.topbar .contact{position:absolute;top:0;height:53px;display:flex;align-items:center;gap:10px;color:#fff;font-size:14px}
.ico-box{width:24px;height:24px;border:1.5px solid #fff;border-radius:6px;display:flex;align-items:center;justify-content:center}
.social-top{position:absolute;right:72px;top:14px;display:flex;gap:8px}
.social-top span{width:26px;height:26px;border:1.5px solid #fff;border-radius:6px;color:#fff;font-size:9px;display:flex;align-items:center;justify-content:center}
.logo-box{left:72px;top:0;width:264px;height:146px;background:#fff;display:flex;align-items:center;justify-content:center}
.brand{font-family:'PT Serif',serif;font-size:40px;color:#1f6f8f;letter-spacing:1px}
.nav{right:69px;top:85px;display:flex;align-items:center;font-size:14px;color:var(--ink)}
.nav a{text-decoration:none;color:inherit;margin-left:32px}
.nav .active{color:var(--accent);border-bottom:2px solid var(--accent);padding-bottom:3px}
.nav .btn-contact{background:var(--accent);color:#fff;border-radius:16px;padding:6px 17px;margin-left:29px}

/* hero */
.hero{left:0;top:149px;width:1200px;height:624px;background:linear-gradient(100deg,#cfd3d6 0%,#e9ecee 30%,#b9bec2 55%,#8f959a 75%,#6e7479 100%)}
.hero-portrait{left:770px;top:149px;width:430px;height:624px;background:linear-gradient(180deg,#3a3134 0%,#2a2b33 60%,#1d2230 100%)}
.hero-panel{left:76px;top:237px;width:670px;height:452px;background:rgba(255,255,255,.72);border-radius:10px;text-align:center}
.hero-panel h1{font-family:'PT Serif',serif;font-weight:400;font-size:62px;line-height:74px;color:#111;margin-top:55px}
.hero-panel p{font-size:14px;line-height:25px;color:#222;width:520px;margin:10px auto 0}
.btn{display:inline-flex;align-items:center;justify-content:center;background:var(--accent);color:#fff;border-radius:26px;text-decoration:none}
.hero-panel .btn{width:209px;height:48px;font-size:20px;margin-top:14px}

/* section heads */
.eyebrow{display:flex;align-items:center;justify-content:center;gap:10px;font-size:16px;color:var(--ink);text-transform:uppercase}
.eyebrow i{display:block;width:44px;height:2px;background:var(--accent);position:relative}
.eyebrow i::after{content:"";position:absolute;width:5px;height:5px;border-radius:50%;background:var(--accent);top:-1.5px}
.eyebrow i.l::after{right:0}.eyebrow i.r::after{left:0}
.sec-title{font-family:'PT Serif',serif;font-weight:400;font-size:42px;color:var(--ink);text-align:center;line-height:1.1}

/* services */
.services{left:0;top:773px;width:1200px;height:1028px;background:var(--soft)}
.svc-card{width:314px;height:314px;background:#fff;text-align:center}
.svc-icon{width:147px;height:147px;border-radius:50%;background:var(--accent);margin:42px auto 0;display:flex;align-items:center;justify-content:center}
.svc-icon svg{width:86px;height:86px;fill:none;stroke:#fff;stroke-width:2;stroke-linecap:round;stroke-linejoin:round}
.svc-card h3{font-size:17px;font-weight:500;color:var(--muted);line-height:24px;margin-top:40px;text-transform:uppercase;padding:0 26px}
.view-more{left:486px;top:1689px;width:229px;height:56px;font-size:21px}

/* about */
.about-photo{left:138px;top:1775px;width:413px;height:550px;border:4px solid #444;border-radius:206px 206px 0 0;background:linear-gradient(180deg,#c9ccd0 0%,#9aa0a6 40%,#2d3140 75%,#1f2431 100%)}
.about-text{left:624px;top:1929px;width:434px}
.about-text .eyebrow{justify-content:flex-start}
.about-text .sec-title{text-align:left;margin-top:4px}
.about-text p{font-size:13.5px;line-height:23.3px;text-align:justify;color:#333;margin-top:10px}
.about-text .btn{width:152px;height:55px;font-size:14px;margin-top:22px}

/* expertise */
.expertise{left:0;top:2365px;width:1200px;height:494px;background:linear-gradient(180deg,var(--pale) 0%,#f0f3f6 60%,#e6ebef 100%)}
.exp-item{width:145px;text-align:center}
.exp-box{width:145px;height:131px;background:#fff;border-radius:3px;display:flex;align-items:center;justify-content:center}
.exp-box svg{width:84px;height:84px;fill:none;stroke:var(--accent-deep);stroke-width:2;stroke-linecap:round;stroke-linejoin:round}
.exp-item p{font-size:19px;line-height:22px;color:var(--ink);margin-top:17px;width:240px;margin-left:-47px}

/* testimonials */
.reviews{left:0;top:2859px;width:1200px;height:497px;background:linear-gradient(180deg,#3e4347 0%,#353a3f 55%,#2e3236 100%)}
.quote-mark{left:0;width:1200px;top:3030px;text-align:center;font-family:'PT Serif',serif;font-size:150px;line-height:150px;color:var(--accent);font-weight:700}
.review-text{left:250px;top:3136px;width:700px;text-align:center;color:#fff;font-size:13.5px;line-height:22px}
.reviewer{left:0;width:1200px;text-align:center;color:#fff;font-family:'PT Serif',serif;font-weight:700}

/* footer */
.footer{left:0;top:3356px;width:1200px;height:427px;background:var(--dark)}
.foot-brand{left:134px;top:3475px;width:231px;text-align:center;font-family:'PT Serif',serif;font-size:44px;color:#fff}
.foot-social{display:flex;gap:13px;left:184px;top:3570px}
.foot-social span{width:35px;height:35px;border-radius:50%;background:#fff;color:var(--dark);font-size:10px;font-weight:600;display:flex;align-items:center;justify-content:center}
.foot-h{font-family:'PT Serif',serif;font-size:24px;color:#fff}
.foot-h::after{content:"";display:block;width:48px;height:1px;background:#888;margin-top:14px}
.foot-links{left:489px;top:3505px;list-style:none;color:#fff;font-size:15px}
.foot-links li{height:32px;display:flex;align-items:center;gap:15px}
.foot-links li::before{content:"";width:7px;height:7px;border-radius:50%;background:#fff}
.foot-contact{left:730px;color:#fff;font-size:15px;display:flex;align-items:center;gap:14px;line-height:19px}
.c-ico{width:36px;height:36px;border-radius:50%;background:#fff;display:flex;align-items:center;justify-content:center;flex:none}
.foot-rule{left:66px;top:3711px;width:1065px;height:1px;background:#777}
.copy{left:0;width:1200px;top:3741px;text-align:center;color:#fff;font-size:13px}
</style>
</head>
<body>

<!-- header -->
<div class="abs topbar">
  <div class="contact" style="left:654px">
    <span class="ico-box"><svg width="13" height="13" viewBox="0 0 24 24"><path fill="#fff" d="M6.6 10.8a15 15 0 0 0 6.6 6.6l2.2-2.2c.3-.3.7-.4 1-.2 1.1.4 2.3.6 3.6.6.6 0 1 .4 1 1V20c0 .6-.4 1-1 1A17 17 0 0 1 3 4c0-.6.4-1 1-1h3.5c.6 0 1 .4 1 1 0 1.3.2 2.5.6 3.6.1.3 0 .7-.2 1z"/></svg></span>
    555-014-2290
  </div>
  <div class="contact" style="left:797px">
    <span class="ico-box"><svg width="13" height="11" viewBox="0 0 24 18"><rect x="1" y="1" width="22" height="16" rx="2" fill="none" stroke="#fff" stroke-width="2"/><path d="M2 2l10 8 10-8" fill="none" stroke="#fff" stroke-width="2"/></svg></span>
    hello@tbrandow.example
  </div>
  <div class="social-top"><span>IG</span><span>FB</span><span>TW</span></div>
</div>
<div class="abs logo-box"><span class="brand">TBrandow</span></div>
<nav class="abs nav">
  <a class="active" href="#">Home</a>
  <a href="#">About</a>
  <a href="#">Services</a>
  <a class="btn-contact" href="#">Contact Us</a>
</nav>

<!-- hero -->
<div class="abs hero" role="img" aria-label="Blurred modern office interior background"></div>
<div class="abs hero-portrait" role="img" aria-label="Portrait of Rosalind in a dark business suit"></div>
<section class="abs hero-panel">
  <h1>EXPERIENCED AND<br>PROFESSIONAL<br>ADVISORS</h1>
  <p>Lorem ipsum dolor sit amet, consectetur adipiscing elit, sed do eiusmod tempor incididunt ut labore et dolore magna aliqua.</p>
  <a class="btn" href="#">Know More</a>
</section>

<!-- services -->
<div class="abs services"></div>
<div class="abs" style="left:0;top:860px;width:1200px">
  <div class="eyebrow"><i class="l"></i>Who we do<i class="r"></i></div>
  <h2 class="sec-title" style="margin-top:4px">OUR SERVICES</h2>
</div>

<div class="abs svc-card" style="left:97px;top:983px">
  <div class="svc-icon"><svg viewBox="0 0 64 64" aria-hidden="true">
    <circle cx="24" cy="24" r="11"/><path d="M20 35v4h8v-4M21 42h6"/>
    <circle cx="24" cy="24" r="4"/><path d="M24 8v3M11 11l2 2M37 11l-2 2M8 24h3M40 24h-3"/>
    <path d="M38 56V46h4v10M45 56V42h4v14M52 56V38h4v18M34 56h24"/><path d="M36 40l8-6 5 3 8-8M53 29h4v4"/>
  </svg></div>
  <h3>Technology Strategy Development</h3>
</div>
<div class="abs svc-card" style="left:441px;top:983px">
  <div class="svc-icon"><svg viewBox="0 0 64 64" aria-hidden="true">
    <circle cx="16" cy="16" r="5"/><circle cx="16" cy="16" r="9" stroke-dasharray="3 3"/>
    <circle cx="47" cy="16" r="10"/><path d="M37 16h20M47 6c-5 6-5 14 0 20M47 6c5 6 5 14 0 20"/>
    <path d="M27 13h7M31 10l3 3-3 3M34 20h-7M30 17l-3 3 3 3"/>
    <circle cx="32" cy="38" r="7"/><path d="M19 58c0-8 6-12 13-12s13 4 13 12z"/>
  </svg></div>
  <h3>Digital Transformation Consulting</h3>
</div>
<div class="abs svc-card" style="left:784px;top:983px">
  <div class="svc-icon"><svg viewBox="0 0 64 64" aria-hidden="true">
    <rect x="6" y="18" width="16" height="30" rx="3"/><rect x="42" y="18" width="16" height="30" rx="3"/>
    <path d="M22 24h20M22 42h20M10 48v8M18 48v8M46 48v8M54 48v8"/>
    <circle cx="32" cy="33" r="5"/><circle cx="32" cy="33" r="8" stroke-dasharray="3 2.5"/>
    <path d="M26 10h12v8H26z"/>
  </svg></div>
  <h3>IT-Business Partnership Development</h3>
</div>
<div class="abs svc-card" style="left:97px;top:1341px">
  <div class="svc-icon"><svg viewBox="0 0 64 64" aria-hidden="true">
    <circle cx="22" cy="20" r="5"/><circle cx="22" cy="20" r="10" stroke-dasharray="3.5 3"/>
    <circle cx="42" cy="42" r="5"/><circle cx="42" cy="42" r="10" stroke-dasharray="3.5 3"/>
    <path d="M40 8a16 16 0 0 1 14 14M54 22l2-6M54 22l-6-1"/>
    <path d="M24 56A16 16 0 0 1 10 42M10 42l-2 6M10 42l6 1"/>
  </svg></div>
  <h3>Organizational Change Management</h3>
</div>
<div class="abs svc-card" style="left:441px;top:1341px">
  <div class="svc-icon"><svg viewBox="0 0 64 64" aria-hidden="true">
    <rect x="10" y="8" width="32" height="46" rx="3"/><path d="M20 6h12v6H20z"/>
    <rect x="16" y="18" width="5" height="5"/><path d="M25 20h12"/>
    <rect x="16" y="28" width="5" height="5"/><path d="M25 30h12"/>
    <rect x="16" y="38" width="5" height="5"/><path d="M25 40h8"/>
    <circle cx="46" cy="46" r="9"/><circle cx="46" cy="46" r="12" stroke-dasharray="3 3"/><path d="M42 46l3 3 5-6"/>
  </svg></div>
  <h3>Program and Project Oversight</h3>
</div>
<div class="abs svc-card" style="left:784px;top:1341px">
  <div class="svc-icon"><svg viewBox="0 0 64 64" aria-hidden="true">
    <path d="M16 28a10 10 0 0 1 8-14 12 12 0 0 1 22 0 10 10 0 0 1 4 18"/>
    <circle cx="18" cy="40" r="5"/><circle cx="18" cy="40" r="9" stroke-dasharray="3 3"/>
    <circle cx="42" cy="36" r="7"/><path d="M30 58c0-8 5-12 12-12s12 4 12 12"/><path d="M42 46v12"/>
  </svg></div>
  <h3>Advisory Services for CIOs and IT Executives</h3>
</div>
<a class="abs btn view-more" href="#">View More</a>

<!-- about -->
<div class="abs about-photo" role="img" aria-label="Portrait of Rosalind smiling in an arched frame"></div>
<section class="abs about-text">
  <div class="eyebrow">Who we are<i class="r"></i></div>
  <h2 class="sec-title">ABOUT US</h2>
  <p>Rosalind Brandow is a seasoned leader with a remarkable 40-year career in the travel industry, including 20 transformative years at Bluecrest Skyways. As the Senior Vice President of Technology (CIO), Rosalind spearheaded some of the company's most significant technological and strategic transformations, helping Bluecrest Skyways stay at the forefront of innovation in the competitive travel market.</p>
  <a class="btn" href="#">Read More</a>
</section>

<!-- expertise -->
<div class="abs expertise"></div>
<div class="abs" style="left:0;top:2428px;width:1200px">
  <div class="eyebrow"><i class="l"></i>TB<i class="r"></i></div>
  <h2 class="sec-title" style="margin-top:4px">EXPERTISE</h2>
</div>
<div class="abs exp-item" style="left:154px;top:2544px">
  <div class="exp-box"><svg viewBox="0 0 64 64" aria-hidden="true">
    <circle cx="32" cy="26" r="20"/><circle cx="32" cy="26" r="15"/>
    <path d="M32 14v24M22 26l10-4 10 4M27 35l5-2 5 2"/>
    <path d="M18 42l-4 12 6-2 4 5 4-10M46 42l4 12-6-2-4 5-4-10"/>
  </svg></div>
  <p>Airline<br>Expertise</p>
</div>
<div class="abs exp-item" style="left:401px;top:2544px">
  <div class="exp-box"><svg viewBox="0 0 64 64" aria-hidden="true">
    <circle cx="24" cy="26" r="8"/><circle cx="24" cy="26" r="16" stroke-dasharray="4 3"/>
    <circle cx="38" cy="42" r="14"/><circle cx="38" cy="42" r="8"/><circle cx="38" cy="42" r="2"/>
    <path d="M38 42l18-14M50 28h6v6"/>
  </svg></div>
  <p>Enterprise-wide<br>strategic initiatives</p>
</div>
<div class="abs exp-item" style="left:648px;top:2544px">
  <div class="exp-box"><svg viewBox="0 0 64 64" aria-hidden="true">
    <path d="M18 12l12-6 12 6v14l-12 6-12-6zM18 12l12 6 12-6M30 18v14"/>
    <circle cx="48" cy="30" r="4"/><circle cx="48" cy="30" r="8" stroke-dasharray="3 2.5"/>
    <path d="M6 50l10-8h12l8 4H24M6 58l10-4h14l20-10"/>
  </svg></div>
  <p>Technology Products<br>and services</p>
</div>
<div class="abs exp-item" style="left:895px;top:2544px">
  <div class="exp-box"><svg viewBox="0 0 64 64" aria-hidden="true">
    <path d="M28 6l20 7v14c0 14-9 22-20 27C17 49 8 41 8 27V13z"/>
    <path d="M28 12l14 5v10c0 10-6 16-14 20"/>
    <path d="M17 26h5v12h-5zM22 27l4-7c2 0 3 2 2 5h5v7l-2 6h-9"/>
    <circle cx="48" cy="44" r="8"/><path d="M44 44l3 3 5-6M44 51l-2 9 6-3 6 3-2-9"/>
  </svg></div>
  <p>Strategy and<br>Change leadership</p>
</div>

<!-- testimonials -->
<div class="abs reviews" role="img" aria-label="Dim background of an airliner above the clouds"></div>
<div class="abs" style="left:0;top:2933px;width:1200px">
  <div class="eyebrow" style="color:#fff"><i class="l"></i>Testimonials<i class="r"></i></div>
  <h2 class="sec-title" style="color:#fff;margin-top:4px">CUSTOMER REVIEWS</h2>
</div>
<div class="abs quote-mark">&ldquo;</div>
<svg class="abs" style="left:193px;top:3146px" width="16" height="26" viewBox="0 0 16 26"><path d="M14 2L3 13l11 11" fill="none" stroke="#00A9DD" stroke-width="3"/></svg>
<svg class="abs" style="left:984px;top:3146px" width="16" height="26" viewBox="0 0 16 26"><path d="M2 2l11 11L2 24" fill="none" stroke="#00A9DD" stroke-width="3"/></svg>
<p class="abs review-text">Rosalind is a decisive and fair leader who exemplifies strength, wisdom, and empathy. She always possesses a clear vision for the future and is willing to make bold decisions which are grounded in data, expertise, and intuition while remaining open to diverse perspectives.</p>
<div class="abs reviewer" style="top:3222px;font-size:16px">MARTIN ELLISON</div>
<div class="abs reviewer" style="top:3248px;font-size:14px">CEO Veyra Labs</div>

<!-- footer -->
<footer class="abs footer"></footer>
<div class="abs foot-brand">TBrandow</div>
<div class="abs foot-social"><span>FB</span><span>TW</span><span>IG</span></div>
<div class="abs foot-h" style="left:489px;top:3431px">LINKS</div>
<ul class="abs foot-links"><li>About</li><li>Services</li><li>Contact Us</li></ul>
<div class="abs foot-h" style="left:730px;top:3431px">CONTACT US</div>
<div class="abs foot-contact" style="top:3507px">
  <span class="c-ico"><svg width="16" height="20" viewBox="0 0 16 20"><path d="M8 0a8 8 0 0 0-8 8c0 6 8 12 8 12s8-6 8-12a8 8 0 0 0-8-8zm0 11a3 3 0 1 1 0-6 3 3 0 0 1 0 6z" fill="#333538"/></svg></span>
  <span>223,Lorem ipsum<br>Lorem ipsum,Lorem ipsum.</span>
</div>
<div class="abs foot-contact" style="top:3569px">
  <span class="c-ico"><svg width="18" height="18" viewBox="0 0 24 24"><path fill="#333538" d="M6.6 10.8a15 15 0 0 0 6.6 6.6l2.2-2.2c.3-.3.7-.4 1-.2 1.1.4 2.3.6 3.6.6.6 0 1 .4 1 1V20c0 .6-.4 1-1 1A17 17 0 0 1 3 4c0-.6.4-1 1-1h3.5c.6 0 1 .4 1 1 0 1.3.2 2.5.6 3.6.1.3 0 .7-.2 1z"/></svg></span>
  <span>8888 888 888</span>
</div>
<div class="abs foot-contact" style="top:3621px">
  <span class="c-ico"><svg width="18" height="14" viewBox="0 0 24 18"><rect x="1" y="1" width="22" height="16" rx="2" fill="#333538"/><path d="M2 2l10 8 10-8" fill="none" stroke="#fff" stroke-width="2"/></svg></span>
  <span>hello@tbrandow.example</span>
</div>
<div class="abs foot-rule"></div>
<div class="abs copy">© 2025 Company Name, Inc. All Rights Reserved.</div>

</body>
</html>
```